Website Redesign - Glow Packs (2 - Pages)

We want a new website that is improved from our first website. Here is an example of a better website: http://www.gleamforte.example/
See our logo attached for design start.
Page 1:
We want a website that looks as good as this but want the following features:
- Top Bar with following Text: Whitening Kits, Whitening Pens, Pura Pulse, Pura Bristle, Accessories & Refills, Instructions, Contact Us
- Right Justified @ top My Account, Checkout
- Static top page image with our ultimate kit photo (attached: Glow Packs - Ultimate Kit.jpg) and an "Order Now" yellow button on the page (See www.velmoraharvest.example for example)
- Five Categories (Teeth Whitening Kits, Teeth Whitening Pens, Pura Pulse, Pura Bristle, Accessories & Refills) all accompanied with pictures and a text bar with name at bottom of pictures... Pura Pulse is a sonic facial brush (don't currently have picture, a filler picture is fine). Pura Bristle is an electronic tooth brush (again don't have product photo)
- Three Pictures Side by Side Pictures to explain product "Save Money", "Whiten Like a Dentist", "Fast Results" (See www.dazzlora.example under why dazz lora with three photos)...
- Reviews ("I love this product!!!", "Works great. Took only 3 sessions to a great smile", "It worked exactly as I had hoped and was simple to use")
- Bottom Order Now Bar (Again, see www.dazzlora.example bottom of page)
Page 2:
Take the instructions and make them part of a cohesive easy to follow page. See Instructions 1, 2, 3

```html
<!DOCTYPE html>
<html lang="en">
<head>
<meta charset="utf-8">
<title>Glow Packs – Accessories &amp; Refills</title>
<link rel="stylesheet" href="https://fonts.googleapis.com/css2?family=Open+Sans:wght@300;400;600;700&family=Oswald:wght@300;400&display=swap">
<style>
:root{
  --blue:#0b5ba9;
  --blue-deep:#0a4f97;
  --blue-link:#1a6fc4;
  --footer-head:#55b3f2;
  --yellow:#f7b52a;
  --yellow-dark:#d8941a;
  --ink:#3b3b3b;
  --muted:#8a8a8a;
  --cta:#4b4b4b;
  --white:#ffffff;
}
*{margin:0;padding:0;box-sizing:border-box}
html,body{width:843px;height:1200px;overflow:hidden}
body{position:relative;font-family:"Open Sans",Arial,sans-serif;background:var(--white);color:var(--ink)}
.abs{position:absolute}

/* header */
.site-header{left:0;top:0;width:843px;height:62px;background:var(--blue)}
.brand{left:140px;top:22px;color:var(--white);font-size:17px;font-weight:400;letter-spacing:.5px}
.account-links{right:140px;top:12px;display:flex;gap:12px;font-size:7.5px;font-weight:600;color:var(--white)}
.main-nav{left:291px;top:42px;display:flex;gap:9px;font-size:7.4px;font-weight:600;color:var(--white)}
.main-nav .active{border-bottom:2px solid #3fa0ea;padding-bottom:8px}
.main-nav .contact{background:var(--yellow);padding:3px 7px;margin-top:-3px;height:14px}

/* hero */
.hero{left:0;top:62px;width:843px;height:259px;background:linear-gradient(180deg,#f4f5f7 0%,#e6e8ec 100%)}
.hero-title{left:141px;top:70px;font-size:33px;font-weight:300;letter-spacing:-1.8px;color:#2d2d2d;line-height:1.2}
.hero-title span{display:block;color:var(--blue);font-weight:400;font-size:36px}
.btn-order{display:block;background:var(--yellow);border-bottom:3px solid var(--yellow-dark);font-family:"Oswald",sans-serif;font-size:12px;color:#3a2a05;text-align:center;letter-spacing:.3px}
.hero .btn-order{left:140px;top:159px;width:95px;height:25px;line-height:23px}
.hero-photo{left:415px;top:40px;width:310px;height:190px;border-radius:8px;background:radial-gradient(ellipse at center,#ffffff 0%,#e9ecf1 70%,rgba(230,232,236,0) 100%)}

/* categories */
.categories{left:0;top:321px;width:843px;height:149px;background:var(--blue-deep);box-shadow:0 4px 6px rgba(0,0,0,.15)}
.cat{top:33px;width:120px;margin-left:-60px;text-align:center;color:var(--white);font-size:8.8px;font-weight:600}
.cat-img{width:74px;height:74px;border-radius:50%;margin:0 auto 10px;border:3px solid var(--white);box-shadow:0 3px 0 var(--yellow)}

/* section headings */
.section-head{left:140px;width:563px;text-align:center;font-size:18px;font-weight:400;letter-spacing:-.6px;color:#3a3a3a}
.section-head::before,.section-head::after{content:"";position:absolute;top:50%;width:170px;height:1px;background:#e2e2e2}
.section-head::before{left:0}.section-head::after{right:0}

/* features */
.feature{top:557px;width:168px}
.feature-img{width:168px;height:104px}
.feature h3{margin-top:9px;font-size:11px;font-weight:600;color:var(--blue-link)}
.feature p{margin-top:2px;font-size:6.6px;line-height:1.55;color:var(--muted)}

/* reviews */
.review{top:792px;width:140px;margin-left:-70px;text-align:center}
.avatar{width:78px;height:78px;border-radius:50%;margin:0 auto;border:3px solid #dcdcdc;background:linear-gradient(160deg,#d9dde3,#9aa3ad)}
.review h4{margin-top:9px;font-size:9px;font-weight:600;color:var(--blue-link)}
.review p{margin-top:4px;font-size:8.5px;line-height:1.35;color:#3a3a3a}
.stars{margin-top:6px;display:flex;justify-content:center;gap:1px}

/* call to action */
.cta-bar{left:0;top:966px;width:843px;height:50px;background:var(--cta)}
.cta-text{left:248px;top:8px;font-family:"Oswald",sans-serif;font-weight:300;font-size:24px;color:var(--white);letter-spacing:-.3px}
.cta-bar .btn-order{left:498px;top:12px;width:98px;height:27px;line-height:25px;font-size:13px}

/* footer */
.site-footer{left:0;top:1016px;width:843px;height:184px;background:linear-gradient(135deg,#0d5fae,#0b56a2)}
.foot-col{top:22px}
.foot-col h5{font-size:10.5px;font-weight:400;color:var(--footer-head);margin-bottom:6px}
.foot-col li{list-style:none;font-size:7.6px;color:var(--white);line-height:15.5px}
.social li{display:flex;align-items:center;gap:8px;line-height:17px}
.social i{display:inline-block;width:11px;height:11px;border-radius:50%;background:var(--white)}
.contact-col li{line-height:12px}
.contact-col .gap{margin-top:3px}
.foot-brand{left:573px;top:115px;font-size:16px;color:var(--white)}
.copyright{left:141px;top:163px;font-size:7.5px;color:#dbe8f6}
</style>
</head>
<body>

<header class="site-header abs">
  <div class="brand abs">GLOW PACKS</div>
  <div class="account-links abs"><span>&#9679; My Account</span><span>&#9656; Check Out</span></div>
  <nav class="main-nav abs">
    <span class="active">Whitening Kits</span><span>Whitening Pens</span><span>Pura Pulse</span><span>Pura Bristle</span><span>Accessories &amp; Refills</span><span>Instructions</span><span class="contact">Contact Us</span>
  </nav>
</header>

<section class="hero abs">
  <h1 class="hero-title abs">Accessories &amp; Refills<span>By Glow Packs</span></h1>
  <a class="btn-order abs">ORDER NOW</a>
  <div class="hero-photo abs" role="img" aria-label="Ultimate kit product photo: whitening tray, LED light, gel syringe, brush and pre-treatment bottle"></div>
</section>

<section class="categories abs">
  <div class="cat abs" style="left:210px"><div class="cat-img" role="img" aria-label="Teeth whitening kits photo" style="background:linear-gradient(160deg,#f1f3f6,#aab3bd)"></div>Teeth Whitening Kits</div>
  <div class="cat abs" style="left:314px"><div class="cat-img" role="img" aria-label="Pura Pulse photo" style="background:linear-gradient(160deg,#e8a0a6,#b5253a)"></div>Pura Pulse</div>
  <div class="cat abs" style="left:422px"><div class="cat-img" role="img" aria-label="Teeth whitening pens photo" style="background:linear-gradient(160deg,#ffffff,#dfe6ee)"></div>Teeth Whitening Pens</div>
  <div class="cat abs" style="left:530px"><div class="cat-img" role="img" aria-label="Pura Bristle photo" style="background:linear-gradient(160deg,#cfe6fb,#2f7fd8)"></div>Pura Bristle</div>
  <div class="cat abs" style="left:633px"><div class="cat-img" role="img" aria-label="Accessories and refills photo" style="background:linear-gradient(160deg,#ffffff,#c8d3e2)"></div>Accessories &amp; Refills</div>
</section>

<h2 class="section-head abs" style="top:511px">Why Glow Packs</h2>

<article class="feature abs" style="left:166px">
  <div class="feature-img" role="img" aria-label="Hands using a calculator over banknotes" style="background:linear-gradient(135deg,#c9c3b8,#5b5d66)"></div>
  <h3>Save Money</h3>
  <p>Lorem ipsum dolor sit amet, consectetuer adipiscing elit, sed diam nonummy nibh euismod tincidunt ut laoreet dolore magna.</p>
</article>
<article class="feature abs" style="left:338px">
  <div class="feature-img" role="img" aria-label="Dentist and patient smiling" style="background:linear-gradient(135deg,#d8cbbd,#a7c2b8)"></div>
  <h3>Whiten Like a Dentist</h3>
  <p>Lorem ipsum dolor sit amet, consectetuer adipiscing elit, sed diam nonummy nibh euismod tincidunt ut laoreet dolore magna.</p>
</article>
<article class="feature abs" style="left:509px">
  <div class="feature-img" role="img" aria-label="Rising chart line with victory hand signs" style="background:linear-gradient(135deg,#163f6f,#3f7cc4)"></div>
  <h3>Fast Results</h3>
  <p>Lorem ipsum dolor sit amet, consectetuer adipiscing elit, sed diam nonummy nibh euismod tincidunt ut laoreet dolore magna.</p>
</article>

<h2 class="section-head abs" style="top:740px">Clients Reviews</h2>

<div class="review abs" style="left:267px">
  <div class="avatar" role="img" aria-label="Reviewer portrait"></div>
  <h4>Nora Bellamy</h4>
  <p>I Love This Product !</p>
  <div class="stars"><svg width="46" height="8" viewBox="0 0 50 9"><g fill="#f5c518"><path id="s" d="M4.5 0l1.1 3.2H9L6.3 5.2l1 3.3-2.8-2-2.8 2 1-3.3L0 3.2h3.4z"/><use href="#s" x="10"/><use href="#s" x="20"/><use href="#s" x="30"/><use href="#s" x="40"/></g></svg></div>
</div>
<div class="review abs" style="left:416px">
  <div class="avatar" role="img" aria-label="Reviewer portrait"></div>
  <h4>Tessa Marlowe</h4>
  <p>It Worked Exactly As I Had Hoped And Was Simple To Use</p>
  <div class="stars"><svg width="46" height="8" viewBox="0 0 50 9"><g fill="#f5c518"><use href="#s"/><use href="#s" x="10"/><use href="#s" x="20"/><use href="#s" x="30"/></g><use href="#s" x="40" fill="#777"/></svg></div>
</div>
<div class="review abs" style="left:563px">
  <div class="avatar" role="img" aria-label="Reviewer portrait"></div>
  <h4>Ruben Castell</h4>
  <p>Works Great Took Only 3 Sessions To A Great Smile</p>
  <div class="stars"><svg width="46" height="8" viewBox="0 0 50 9"><g fill="#f5c518"><use href="#s"/><use href="#s" x="10"/><use href="#s" x="20"/></g><g fill="#777"><use href="#s" x="30"/><use href="#s" x="40"/></g></svg></div>
</div>

<section class="cta-bar abs">
  <div class="cta-text abs">Get Your Glow Pack Today !</div>
  <svg class="abs" style="left:466px;top:19px" width="24" height="12" viewBox="0 0 24 12"><path d="M0 6h18" stroke="#fff" stroke-width="1.4" stroke-dasharray="2 2"/><path d="M16 1l6 5-6 5" fill="none" stroke="#fff" stroke-width="1.4"/></svg>
  <a class="btn-order abs">ORDER NOW</a>
</section>

<footer class="site-footer abs">
  <div class="foot-col abs" style="left:141px">
    <h5>Teeth Whitening Products</h5>
    <ul><li>Teeth Whitening Kits</li><li>Teeth Whitening Pens</li><li>Pura Pulse</li><li>Pura Bristle</li><li>Accessories &amp; Refills</li></ul>
  </div>
  <div class="foot-col abs" style="left:319px">
    <h5>Site Navigation</h5>
    <ul><li>Whitening Kits</li><li>Whitening Pens</li><li>Pura Pulse</li><li>Pura Bristle</li><li>Accessories &amp; Refills</li></ul>
  </div>
  <div class="foot-col social abs" style="left:458px">
    <h5>Social Media</h5>
    <ul><li><i></i>Chatterly</li><li><i></i>Workwise</li><li><i></i>Chirpline</li><li><i></i>Reelhub</li><li><i></i>Circlo</li></ul>
  </div>
  <div class="foot-col contact-col abs" style="left:571px">
    <h5>Contact us</h5>
    <ul>
      <li>514 Larkfield Ave. Brenton, Nc</li><li>20417</li>
      <li>Phone (555) 014-2290,</li><li>Email : hello@glowpacks.example</li>
      <li class="gap">General Enquiries: 555-010-7781</li><li>Technical Enquiries: 555-010-3362</li>
    </ul>
  </div>
  <div class="foot-brand abs">GLOW PACKS</div>
  <div class="copyright abs">Professional Teeth Whitening Kits By Glow Packs - © Copyright 2014</div>
</footer>

</body>
</html>
```